Brightwell Consulting Business Card Design

Business Card Design for Brightwell Consulting. Brightwell Consulting is a boutique consultancy based in Atlanta, GA., that specializes in marketing strategy, organization planning, and leadership development. We provide solutions for small businesses and startups as well as Summit 400 companies.

http://brightwellconsulting.example/

Target Market(s)

We provide solutions for small businesses and startups as well as Summit 400 companies.

Industry/Entity Type

Consulting

Contact Information for Business Card

Two sided business card with priority on contact information, logo, tag line (Inspiration to Dream More, Do More, Become More)

Colors

Designer to choose colors to be used in the design.

Requirements
Must have
• contact information, logo, tag line (Inspiration to Dream More, Do More, Become More)
• Simple no over communication.
Nice to have
• I would like to see different placements of logo and creative use of both sides of the card
Should not have
• Do not put too much information on the card.

```html
<!DOCTYPE html>
<html lang="en">
<head>
<meta charset="utf-8">
<title>Brightwell Consulting – Business Card</title>
<link rel="stylesheet" href="https://fonts.googleapis.com/css2?family=Lobster&family=Open+Sans:wght@400;600&display=swap">
<style>
  :root {
    --page-bg: #e4e2df;
    --panel-dark: #353535;
    --panel-light: #f3f2ef;
    --ink-light: #ffffff;
    --ink-dark: #2f2f2f;
    --rule: #6a6a6a;
  }
  html, body {
    margin: 0;
    width: 1200px;
    height: 900px;
    overflow: hidden;
    background: var(--page-bg);
  }
  .card {
    position: absolute;
    left: 100px;
    top: 142px;
    width: 1000px;
    height: 617px;
    display: flex;
    box-shadow: 0 10px 30px rgba(0,0,0,0.18);
  }
  .card__info {
    position: relative;
    width: 498px;
    height: 100%;
    background: var(--panel-dark);
    color: var(--ink-light);
  }
  .card__brand {
    position: relative;
    flex: 1;
    background: var(--panel-light);
    display: flex;
    align-items: center;
    justify-content: center;
  }
  .person {
    position: absolute;
    right: 59px;
    top: 52px;
    text-align: right;
  }
  .person__name {
    font-family: "Lobster", cursive;
    font-size: 41px;
    line-height: 1.1;
    margin: 0;
    font-weight: 400;
  }
  .person__title {
    font-family: "Open Sans", sans-serif;
    font-size: 25px;
    margin: 0;
  }
  .contact {
    position: absolute;
    right: 34px;
    top: 200px;
    list-style: none;
    margin: 0;
    padding: 0;
    font-family: "Open Sans", sans-serif;
    font-size: 26px;
    text-align: right;
  }
  .contact li {
    height: 37px;
    display: flex;
    align-items: center;
    justify-content: flex-end;
    gap: 8px;
  }
  .contact svg { width: 22px; height: 22px; flex: none; }
  .divider {
    position: absolute;
    left: 51px;
    width: 420px;
    top: 368px;
    height: 1px;
    background: var(--rule);
  }
  .tagline {
    position: absolute;
    right: 59px;
    top: 418px;
    margin: 0;
    font-family: "Lobster", cursive;
    font-size: 36px;
    line-height: 45px;
    text-align: right;
    letter-spacing: 0.5px;
  }
  .logo {
    display: flex;
    align-items: center;
    gap: 14px;
  }
  .logo__mark {
    width: 18px;
    height: 18px;
    background: var(--ink-dark);
  }
  .logo__name {
    font-family: "Open Sans", sans-serif;
    font-weight: 600;
    font-size: 40px;
    color: var(--ink-dark);
  }
</style>
</head>
<body>
  <div class="card">
    <section class="card__info">
      <div class="person">
        <h1 class="person__name">Daniel Harper</h1>
        <p class="person__title">Managing Director</p>
      </div>
      <ul class="contact">
        <li>(044)555010247
          <svg viewBox="0 0 24 24" aria-hidden="true"><path fill="#fff" d="M6.6 10.8a15 15 0 0 0 6.6 6.6l2.2-2.2c.3-.3.7-.4 1-.2 1.1.4 2.3.6 3.6.6.6 0 1 .4 1 1V20c0 .6-.4 1-1 1A17 17 0 0 1 3 4c0-.6.4-1 1-1h3.5c.6 0 1 .4 1 1 0 1.3.2 2.5.6 3.6.1.3 0 .7-.2 1z"/></svg>
        </li>
        <li>hello@brightwellmail.example
          <svg viewBox="0 0 24 24" aria-hidden="true"><rect x="2" y="5" width="20" height="14" fill="#fff"/><polyline points="2,5 12,13 22,5" fill="none" stroke="#353535" stroke-width="2"/></svg>
        </li>
        <li>www.brightwellconsulting.example
          <svg viewBox="0 0 24 24" aria-hidden="true"><circle cx="12" cy="12" r="9" fill="#fff"/><path d="M7 9c2 0 3 1 3 3s2 2 2 4M15 6c-1 2 1 3 3 3" fill="none" stroke="#353535" stroke-width="1.8"/></svg>
        </li>
      </ul>
      <div class="divider"></div>
      <p class="tagline">Inspiration to<br>Dream More<br>Do More, Become More</p>
    </section>
    <section class="card__brand">
      <div class="logo">
        <span class="logo__mark"></span>
        <span class="logo__name">Brightwell Consulting</span>
      </div>
    </section>
  </div>
</body>
</html>
```